Radiant Crossing - An Exciting Mission & Book Cover Project

Help me to inspire people to live their best life! This is a mission, not just a design project.
I need a Book Cover designed to keep me inspired on the process of writing my book.
Book Title: Radiant Crossing
Tag Line: Three Simple Steps to get out of your own way, SuperCharge your Life and Step into Purpose!
Author: Marlis Quenby

The three steps are: Ownership, Vision and Action (Not sure if this should be on the front or back of the book cover)

The book is a self-help, motivational book. Personal development.
The cover needs to be strong and capture peoples attention, especially with competing shelf space. I almost see a fire ball of flame or explosion that will grab peoples attention.
My company is The Lantern Institute. I have added the company logo and a few pages of my presentation and topic outline to give an idea.
Maybe: The Lantern Institute logo on back of the cover. website is marlisquenby.com

THOUGHT: People should be able to take a photo of them holding the book cover showing what area of life they want Radiant Crossing in. This is why the front cover must be so visual and powerful that they want to take a photo with it. Ie. Explosion, fire, strong and bold.

Target Market(s)

Anyone who feels stuck and needs to breakthrough and move forward in life.

Industry/Entity Type

Motivation

Font styles to use
Serif
Sans Serif

Colors
ec1f27
f37122
fbed22

Requirements
Must have
• The design must be STRONG, SIMPLE, STAND OUT ON BOOK SHELVES.
Must have an open file to swap the photo and copy out.

Back Cover Page
1) Summary
2) 2-3 testimonials. One sentence.
3) About the Author (maybe with photo)
4) Lantern Institute logo
5) Website: radiantcrossing.com and marlisquenby.com
Nice to have
• If my photo works somewhere that would be great. I will change the photo later.
Added Where's Your Harbor? a nice cover example.
Should not have
• Right now I am writing the summary for the back of the cover. For now use Loreum Ipsum text and 2-3 recommendations. Again, I will get these only later.

```html
<!DOCTYPE html>
<html lang="en">
<head>
<meta charset="utf-8">
<title>Radiant Crossing — Book Cover</title>
<link rel="stylesheet" href="https://fonts.googleapis.com/css2?family=Montserrat:wght@800&family=Barlow+Condensed:wght@500;600;700&display=swap">
<style>
  :root {
    --stage: #000000;
    --paper: #ffffff;
    --ink: #0d0d0d;
    --flame-yellow: #f6c23a;
    --flame-amber: #f39a2c;
    --flame-orange: #f37122;
    --flame-red: #ec5a2a;
    --title-top: #f29a3a;
    --title-bottom: #ee6a30;
  }
  * { box-sizing: border-box; margin: 0; padding: 0; }
  html, body {
    width: 1200px;
    height: 1200px;
    overflow: hidden;
    background: var(--stage);
  }
  .canvas {
    position: relative;
    width: 1200px;
    height: 1200px;
    background: var(--stage);
  }
  .book-cover {
    position: absolute;
    left: 278px;
    top: 102px;
    width: 644px;
    height: 996px;
    background: var(--paper);
    overflow: hidden;
  }
  .cover-art {
    position: absolute;
    left: 0;
    top: 0;
    width: 644px;
    height: 540px;
    background:
      radial-gradient(ellipse 36% 48% at 50% 46%, rgba(255,255,255,0.95) 0%, rgba(255,255,255,0.6) 40%, rgba(255,255,255,0) 70%),
      radial-gradient(ellipse 60% 62% at 50% 50%, var(--flame-red) 0%, var(--flame-orange) 35%, var(--flame-amber) 60%, var(--flame-yellow) 100%);
  }
  .cover-art::after {
    content: "";
    position: absolute;
    left: 0;
    right: 0;
    bottom: 0;
    height: 130px;
    background: linear-gradient(to bottom, rgba(255,255,255,0), var(--paper) 85%);
  }
  .title {
    position: absolute;
    left: 0;
    width: 100%;
    text-align: center;
    line-height: 1;
  }
  .title-first {
    top: 684px;
    font-family: "Montserrat", sans-serif;
    font-weight: 800;
    font-size: 80px;
    letter-spacing: 2px;
    color: var(--ink);
  }
  .title-second {
    top: 768px;
    font-family: "Barlow Condensed", sans-serif;
    font-weight: 700;
    font-size: 104px;
    letter-spacing: 2px;
    background: linear-gradient(to bottom, var(--title-top), var(--title-bottom));
    -webkit-background-clip: text;
    background-clip: text;
    color: transparent;
  }
  .tagline {
    position: absolute;
    top: 880px;
    left: 0;
    width: 100%;
    text-align: center;
    font-family: "Barlow Condensed", sans-serif;
    font-weight: 600;
    font-size: 25px;
    line-height: 36px;
    color: var(--ink);
  }
  .author {
    position: absolute;
    top: 1000px;
    left: 0;
    width: 100%;
    text-align: center;
    font-family: "Barlow Condensed", sans-serif;
    font-weight: 600;
    font-size: 62px;
    letter-spacing: 1px;
    line-height: 1;
    color: var(--ink);
  }
</style>
</head>
<body>
  <main class="canvas">
    <section class="book-cover">
      <div class="cover-art" role="img" aria-label="The author in a navy blazer stepping through a wall of shattered yellow and orange fragments bursting outward"></div>
      <h1 class="title title-first" style="top:582px">RADIANT</h1>
      <p class="title title-second" style="top:658px">CROSSING</p>
      <p class="tagline" style="top:780px">3 SIMPLE STEPS to get out of your own way,<br>SuperCharge your Life and Step into Purpose!</p>
      <p class="author" style="top:884px">MARLIS QUENBY</p>
    </section>
  </main>
</body>
</html>
```